Varga Lillas Physiotherapy Business Card Vienna

We need a business card design for a newly created Physiotherapy company based in Vienna Austria.
We seek a simple, modern, minimalist design without too much color variation. The font should look young/fresh, but definitely not childish or so. Since we are a starting Business, we currently haven't got a logo, if you feel like a logo would fit your design, feel free to use one, but it's not necessary.
Target Market(s)
Healthcare, young and elderly people with mobility issues
Industry/Entity Type
Health And Wellness
Contact Information for Business Card
Name: Lilla Varga
Title description: Physiotherapist
Phone num: +43 664 5290 4816
e-mail: lilla.praxis@brelomail.com
Colors
Designer to choose colors to be used in the design.
Requirements
Must have
- Final design language must be in German, basically, the Title Description needs to be "Physiotherapeutin" the other details remain as in the English Language.
Nice to have
- Simple, modern, minimalist design
Should not have
- too many colors, Obvious use of a skeleton, skull, spline

```html
<!DOCTYPE html>
<html lang="de">
<head>
<meta charset="utf-8">
<title>Lilla Varga – Physiotherapeutin</title>
<link href="https://fonts.googleapis.com/css2?family=Oswald:wght@200;700&family=Open+Sans:wght@400&display=swap" rel="stylesheet">
<style>
  :root {
    --backdrop: #e6e4e1;
    --card: #ffffff;
    --ink: #111111;
  }
  html, body {
    margin: 0;
    padding: 0;
    width: 1200px;
    height: 1200px;
    overflow: hidden;
    background: var(--backdrop);
  }
  .canvas {
    position: relative;
    width: 1200px;
    height: 1200px;
  }
  .business-card {
    position: absolute;
    left: 280px;
    top: 105px;
    width: 640px;
    height: 990px;
    background: var(--card);
    box-shadow: 0 6px 24px rgba(0,0,0,0.12);
  }
  .card-frame {
    position: absolute;
    inset: 0;
    width: 640px;
    height: 990px;
  }
  .card-frame line {
    stroke: var(--ink);
    stroke-width: 4;
    stroke-linecap: butt;
  }
  .headline {
    position: absolute;
    left: 78px;
    top: 78px;
    margin: 0;
    color: var(--ink);
    font-family: "Oswald", "Arial Narrow", sans-serif;
    text-transform: uppercase;
    line-height: 0.9;
  }
  .headline .job-title {
    display: block;
    font-weight: 700;
    font-size: 112px;
    letter-spacing: 0.01em;
  }
  .headline .person-name {
    display: block;
    font-weight: 200;
    font-size: 112px;
    letter-spacing: 0.01em;
  }
  .contact-block {
    position: absolute;
    left: 78px;
    bottom: 78px;
    margin: 0;
    color: var(--ink);
    font-family: "Open Sans", Arial, sans-serif;
    font-size: 21px;
    line-height: 1.45;
    letter-spacing: 0.14em;
  }
  .contact-block span {
    display: block;
  }
</style>
</head>
<body>
<div class="canvas">
  <section class="business-card">
    <svg class="card-frame" viewBox="0 0 640 990" aria-hidden="true">
      <line x1="40" y1="40" x2="600" y2="40"/>
      <line x1="600" y1="38" x2="600" y2="80"/>
      <line x1="600" y1="190" x2="600" y2="420"/>
      <line x1="600" y1="520" x2="600" y2="952"/>
      <line x1="40" y1="950" x2="600" y2="950"/>
      <line x1="40" y1="38" x2="40" y2="390"/>
      <line x1="40" y1="480" x2="40" y2="760"/>
      <line x1="40" y1="870" x2="40" y2="952"/>
    </svg>
    <h1 class="headline">
      <span class="job-title">Physiothe</span>
      <span class="job-title">rapeutin</span>
      <span class="person-name">Lilla</span>
      <span class="person-name">Varga</span>
    </h1>
    <p class="contact-block">
      <span class="contact-role">Physiotherapist</span>
      <span class="contact-phone">+43 664 5290 4816</span>
      <span class="contact-email">lilla.praxis@brelomail.com</span>
    </p>
  </section>
</div>
</body>
</html>
```